Italian Restaurant Responsive Wordpress Website Design

Italian Restaurant is looking to create a new responsive website design based on some Wordpress templates that have been selected as favourites. We want to base the influence of the design off a business card that was recently created (attached below).
The design should be based of these templates that will be purchased when selected. All templates are responsive. Please read details of templates to learn more about their functions and features. After we select the designs we can deliver the customizable PSD files.
http://layoutgrove.example/item/tangle-responsive-restaurant-wordpress-theme/full_screen_preview/7316420
http://cloakdesigns.example/themes/?theme=Bellamo
http://themes.loftbrick.example/rigatta/
http://www.tablecraftkit.example/
Pages required
Homepage
-Navigation
-Contact info always accessible on all responsive viewports. You may have to include a design for Contact info on mobile viewport to the top of the page.
-Hours of Operation
About Page
Menu
-Styling of content will be very identical to menu's. That will be provided once I receive a copy.
Gallery
Contact Page
-Show a map, Contact Details and a Contact/Feedback Form
We are open to any designs that you want to lay on top of these Template designs. The current site is: www.quintavela.example If you want an indication of content.
Any questions please ask! Enjoy!
Updates
Hello Everyone. I just updated the menu being used in the restaurant as well as the fonts that are being used as we speak. Any questions please email me. Cheers.
Target Market(s)
The Target Market is families and a more distinguished crowd. They offer valued gourmet food but are located in a very high end neighbourhood. Want to deliver home made cuisine that's approachable but yet considered gourmet.
Industry/Entity Type
Business
Look and feel
Each slider illustrates characteristics of the customer's brand and the style your logo design should communicate.

```html
<!DOCTYPE html>
<html lang="en">
<head>
<meta charset="utf-8">
<title>Quinta Vela – Mobile Home</title>
<link href="https://fonts.googleapis.com/css2?family=Lato:ital,wght@0,300;0,400;0,700;0,900;1,400&display=swap" rel="stylesheet">
<style>
:root{
  --stage:#0d0d0d;
  --red:#b3261e;
  --red-dark:#8f1c16;
  --brown:#3b3029;
  --brown-deep:#2f2621;
  --cream:#f3efe6;
  --paper:#ffffff;
  --light:#f6f6f4;
  --ink:#3a3330;
  --muted:#8b8480;
  --line:#e2dfda;
}
*{box-sizing:border-box;margin:0;padding:0}
html,body{width:1200px;height:3429px;overflow:hidden;background:var(--stage)}
body{font-family:'Lato',sans-serif;color:var(--ink)}
.site{width:680px;height:3429px;margin:0 auto;background:var(--paper);display:flex;flex-direction:column}

/* hero */
.hero{position:relative;height:633px;overflow:hidden}
.hero-photo{position:absolute;inset:0;background:radial-gradient(ellipse at 40% 45%,#f6e9c4 0%,#e8cf95 35%,#c79a5a 70%,#7c5a36 100%)}
.brand{position:absolute;top:40px;left:0;right:0;display:flex;justify-content:center;align-items:center;gap:14px}
.brand-dot{width:26px;height:26px;border-radius:50%;background:var(--red)}
.brand-name{font-weight:900;font-size:40px;color:var(--red);letter-spacing:1px}
.menu-toggle{position:absolute;top:0;right:0;width:100px;height:93px;background:var(--red);display:flex;align-items:center;justify-content:center}
.main-nav{position:absolute;top:93px;right:0;width:264px;height:433px;background:rgba(47,38,33,.9);padding:16px 0 0 30px;z-index:3}
.main-nav a{display:block;color:#fff;text-decoration:none;font-size:29px;font-weight:700;line-height:67px;text-transform:uppercase}
.slide-arrow{position:absolute;top:296px;width:46px;height:64px;background:rgba(255,255,255,.85);display:flex;align-items:center;justify-content:center}
.slide-arrow.prev{left:0}
.slide-arrow.next{right:0;z-index:2}
.caption{position:absolute;left:0;right:0;top:435px;height:115px;background:rgba(255,255,255,.55);padding:22px 0 0 86px}
.caption h2{font-size:36px;font-weight:900;color:var(--brown-deep);letter-spacing:.5px}
.caption p{font-size:17px;font-weight:700;color:var(--brown-deep);margin-top:10px;letter-spacing:.5px;white-space:nowrap}

/* contact bar */
.contact-bar{height:93px;background:var(--brown);display:flex;justify-content:center;align-items:center;gap:50px}
.contact-btn{width:243px;height:60px;background:var(--red);color:#fff;display:flex;align-items:center;gap:18px;padding-left:22px;font-size:20px;font-weight:700;text-transform:uppercase}

/* welcome */
.welcome{height:427px;text-align:center;padding:30px 38px 0}
.welcome h1{font-size:31px;font-weight:400;color:var(--ink)}
.welcome .lead{font-size:20px;line-height:1.5;margin-top:22px;color:var(--ink)}
.welcome .body{font-size:16.5px;line-height:1.62;color:#6a635f;margin-top:24px}
.read-more{display:inline-flex;align-items:center;gap:10px;font-size:15px;color:#6a635f;margin-top:28px}

/* section title */
.section-title{font-size:27px;font-weight:700;text-transform:uppercase;text-align:center;color:var(--ink);letter-spacing:.5px}

/* recommended */
.recommended{height:606px;background:var(--cream);padding:36px 27px 0}
.cards{display:grid;grid-template-columns:1fr 1fr;gap:23px;margin-top:34px}
.dish-card{background:var(--paper);height:426px;text-align:center;padding:10px 10px 0}
.dish-photo{height:160px;background:linear-gradient(135deg,#b9753d 0%,#e3c4a0 45%,#8a4b22 75%,#5d7a36 100%)}
.dish-card h3{font-size:20px;font-weight:400;margin-top:22px}
.dish-card p{font-size:16px;line-height:1.45;color:#6a635f;margin:18px 8px 0}
.dish-rule{margin:20px 12px 0;border-top:1px solid var(--line);position:relative;height:30px}
.dish-rule svg{position:absolute;left:50%;top:-10px;transform:translateX(-50%);background:var(--paper)}
.price{font-size:21px;color:var(--ink)}

/* blog */
.blog{height:666px;background:var(--light);padding:50px 40px 0}
.post{display:flex;gap:16px;margin-top:42px}
.post + .post{margin-top:60px}
.post-media{width:67px;flex:none}
.post-thumb{height:64px;background:linear-gradient(135deg,#d6a25f,#8d5a2e)}
.post-date{height:68px;background:var(--red);color:#fff;text-align:center;padding-top:4px}
.post-date span{display:block;font-size:14px;text-transform:uppercase}
.post-date strong{display:block;font-size:32px;font-weight:700;line-height:1}
.post h3{font-size:23px;font-weight:400;color:var(--ink)}
.post .byline{font-size:16px;color:var(--muted);margin-top:4px}
.post .byline em{font-style:normal;color:var(--ink)}
.post p{font-size:16.5px;line-height:1.55;color:var(--muted);margin-top:18px}
.post .read-more{margin-top:24px}

/* hours */
.hours{height:548px;background:var(--paper);padding:44px 0 0}
.hours-table{width:543px;margin:66px auto 0;border-collapse:collapse}
.hours-table td{font-size:19px;color:#7a736f;height:53px;border-bottom:1px solid var(--line)}
.hours-table tr:first-child td{border-top:1px solid var(--line)}
.hours-table td.time{text-align:right;color:var(--ink)}

/* newsletter */
.newsletter{height:456px;background:var(--brown);text-align:center;padding:50px 23px 0;color:#fff}
.newsletter h2{font-size:23px;font-weight:400;text-transform:uppercase;letter-spacing:.5px}
.newsletter .sub{font-size:19px;margin-top:6px;color:#e8e2dc}
.email-field{height:67px;background:#564a42;margin-top:32px;text-align:left;padding-left:22px;line-height:67px;font-size:21px;font-style:italic;color:#a39890}
.signup-btn{width:240px;height:57px;background:var(--red);margin:30px auto 0;line-height:57px;font-size:19px;font-weight:700;text-transform:uppercase}
.footer-note{border-top:1px solid #54483f;margin-top:42px;padding-top:34px;font-size:16px;line-height:1.6;color:#d8d0c9}
</style>
</head>
<body>
<div class="site">

  <header class="hero">
    <div class="hero-photo" role="img" aria-label="Photo of a plate of fresh pasta with vegetables"></div>
    <div class="brand"><span class="brand-dot"></span><span class="brand-name">Quinta Vela</span></div>
    <div class="menu-toggle">
      <svg width="40" height="30" viewBox="0 0 40 30"><rect y="0" width="40" height="5" fill="#fff"/><rect y="12" width="40" height="5" fill="#fff"/><rect y="24" width="40" height="5" fill="#fff"/></svg>
    </div>
    <nav class="main-nav">
      <a href="#">Home</a><a href="#">Menus</a><a href="#">About Us</a><a href="#">Groups</a><a href="#">VIP List</a><a href="#">Contact</a>
    </nav>
    <div class="slide-arrow prev"><svg width="16" height="26" viewBox="0 0 16 26"><path d="M13 2 3 13l10 11" fill="none" stroke="#b3261e" stroke-width="4"/></svg></div>
    <div class="slide-arrow next"><svg width="16" height="26" viewBox="0 0 16 26"><path d="M3 2l10 11L3 24" fill="none" stroke="#b3261e" stroke-width="4"/></svg></div>
    <div class="caption">
      <h2>UNIQUE AND DELICIOUS</h2>
      <p>LOREM IPSUM DOLOR SIT AMET, CONSECTETUR</p>
    </div>
  </header>

  <div class="contact-bar">
    <div class="contact-btn">
      <svg width="26" height="26" viewBox="0 0 24 24"><path d="M6.6 10.8a15 15 0 0 0 6.6 6.6l2.2-2.2a1 1 0 0 1 1-.25 11.4 11.4 0 0 0 3.6.57 1 1 0 0 1 1 1V20a1 1 0 0 1-1 1A17 17 0 0 1 3 4a1 1 0 0 1 1-1h3.5a1 1 0 0 1 1 1c0 1.25.2 2.45.57 3.57a1 1 0 0 1-.25 1z" fill="#fff"/></svg>
      Call Now
    </div>
    <div class="contact-btn">
      <svg width="22" height="28" viewBox="0 0 20 28"><path d="M10 0a10 10 0 0 0-10 10c0 7.5 10 18 10 18s10-10.5 10-18A10 10 0 0 0 10 0zm0 14a4 4 0 1 1 0-8 4 4 0 0 1 0 8z" fill="#fff"/></svg>
      Address
    </div>
  </div>

  <section class="welcome">
    <h1>Welcome to Quinta Vela</h1>
    <p class="lead">Quinta Vela welcomes reservations and encourages walk-ins at anytime. Please&nbsp; call anytime.</p>
    <p class="body">Located in the heart of Larkmere West, Quinta Vela is named for the most highly - refined italian flour, our key ingredient in our superior pizza and pasta. Morrone's pride &amp; joy: an italian joint showcasing his Pugliese heritage. Our menu consists mostly of comfort food, offering a restaurant atmosphere for families and making it a tradition. We offer gluten free and whole-wheat options for our Wood Burning pizza and pasta.</p>
    <span class="read-more"><svg width="16" height="10" viewBox="0 0 16 10"><path d="M0 5h13M9 1l4 4-4 4" fill="none" stroke="#6a635f" stroke-width="1.6"/></svg>Read Ahead</span>
  </section>

  <section class="recommended">
    <h2 class="section-title">We Recomended</h2>
    <div class="cards">
      <article class="dish-card">
        <div class="dish-photo" role="img" aria-label="Photo of sliced roast meat with salad greens"></div>
        <h3>Sweet and Sour Steaks</h3>
        <p>Lorem Ipsum. Proin gravida nibh vel velit auctor aliquet. Aenean sollicitudin, lorem quis bibendum auctor,</p>
        <div class="dish-rule"><svg width="36" height="20" viewBox="0 0 36 20"><path d="M4 10q7-8 14 0t14 0" fill="none" stroke="#8b8480" stroke-width="1.6"/></svg></div>
        <div class="price">$12.54</div>
      </article>
      <article class="dish-card">
        <div class="dish-photo" role="img" aria-label="Photo of sliced roast meat with salad greens"></div>
        <h3>Sweet and Sour Steaks</h3>
        <p>Lorem Ipsum. Proin gravida nibh vel velit auctor aliquet. Aenean sollicitudin, lorem quis bibendum auctor,</p>
        <div class="dish-rule"><svg width="36" height="20" viewBox="0 0 36 20"><path d="M4 10q7-8 14 0t14 0" fill="none" stroke="#8b8480" stroke-width="1.6"/></svg></div>
        <div class="price">$12.54</div>
      </article>
    </div>
  </section>

  <section class="blog">
    <h2 class="section-title">Latest Blog</h2>
    <article class="post">
      <div class="post-media">
        <div class="post-thumb" role="img" aria-label="Small photo of a dish"></div>
        <div class="post-date"><span>June</span><strong>25</strong></div>
      </div>
      <div>
        <h3>Image Blog Title Here</h3>
        <div class="byline">By: <em>Marlo Fenwick</em></div>
        <p>Phasellus vehicula justo eget diam posuere sollicitudin eu tincid nulla. curabitur eleifend magna scele lore ipsum is only free text isque placerat vele phasellus just.</p>
        <span class="read-more"><svg width="16" height="10" viewBox="0 0 16 10"><path d="M0 5h13M9 1l4 4-4 4" fill="none" stroke="#6a635f" stroke-width="1.6"/></svg>Read Ahead</span>
      </div>
    </article>
    <article class="post">
      <div class="post-media">
        <div class="post-thumb" role="img" aria-label="Small photo of a dish"></div>
        <div class="post-date"><span>June</span><strong>25</strong></div>
      </div>
      <div>
        <h3>Image Blog Title Here</h3>
        <div class="byline">By: <em>Marlo Fenwick</em></div>
        <p>Phasellus vehicula justo eget diam posuere sollicitudin eu tincid nulla. curabitur eleifend magna scele lore ipsum is only free text isque placerat vele phasellus just.</p>
        <span class="read-more"><svg width="16" height="10" viewBox="0 0 16 10"><path d="M0 5h13M9 1l4 4-4 4" fill="none" stroke="#6a635f" stroke-width="1.6"/></svg>Read Ahead</span>
      </div>
    </article>
  </section>

  <section class="hours">
    <h2 class="section-title">Opening Hours</h2>
    <table class="hours-table">
      <tr><td>Monday :</td><td class="time">11:00am-10:00pm</td></tr>
      <tr><td>Tuesday :</td><td class="time">11:00am-10:00pm</td></tr>
      <tr><td>Wednesday :</td><td class="time">11:00am-11:00pm</td></tr>
      <tr><td>Thursday :</td><td class="time">11:00am-11:00pm</td></tr>
      <tr><td>Friday :</td><td class="time">11:00am-11:00pm</td></tr>
      <tr><td>Saturday :</td><td class="time">11:00am-11:00pm</td></tr>
      <tr><td>Sunday :</td><td class="time">4:30pm - 10:00pm</td></tr>
    </table>
  </section>

  <footer class="newsletter">
    <h2>Sign Up For Our Newsletter</h2>
    <p class="sub">and recieve notifications from us</p>
    <div class="email-field">enter your email</div>
    <div class="signup-btn">Signup Today</div>
    <p class="footer-note">Quinta Vela 218 Larkmere Rd. Westbrook, ON (555) 014-2290<br>Copyright © 2013 Tavola.EX</p>
  </footer>

</div>
</body>
</html>
```